Extra job from Miami Logo design job

This posting is for the winner of the Tessaly Lane Shop logo, we need an example of what the commerce webpage would look like.

Please go here to submit the logo first:

http://jobs.brightpitchworks.com/job.aspx?id=518204.

```html
<!DOCTYPE html>
<html lang="en">
<head>
<meta charset="utf-8">
<title>Tessaly Lane Shop — Storefront</title>
<link href="https://fonts.googleapis.com/css2?family=Cormorant+Garamond:wght@400;500&family=Lato:wght@400;700&display=swap" rel="stylesheet">
<style>
  :root {
    --pink: #e8315a;
    --ink: #1b1e27;
    --ink-soft: #2a2e39;
    --sidebar-text: #d9dbe2;
    --sidebar-muted: #8d919c;
    --paper: #ffffff;
    --card-bg: #f4f2f1;
    --body-text: #6b6e76;
    --heading: #2b2d33;
    --banner-light: #c8b79f;
    --banner-dark: #8a7a66;
    --photo-light: #ece8e6;
    --photo-mid: #d9cfc9;
  }
  * { box-sizing: border-box; margin: 0; padding: 0; }
  html, body { width: 1200px; height: 805px; overflow: hidden; background: var(--paper); }
  body { font-family: "Lato", sans-serif; color: var(--body-text); }

  .page {
    width: 1200px; height: 805px;
    display: grid;
    grid-template-columns: 250px 1fr;
    grid-template-rows: 40px 1fr;
  }

  /* Top utility bar */
  .utility-bar {
    grid-column: 1 / 3;
    background: var(--pink);
    display: flex; align-items: center; justify-content: space-between;
    padding: 0 22px; color: #fff; font-size: 12px;
  }
  .utility-links { display: flex; list-style: none; }
  .utility-links li { padding: 0 16px; border-right: 1px solid rgba(255,255,255,.55); }
  .utility-links li:first-child { padding-left: 0; }
  .utility-links li:last-child { border-right: 0; }
  .utility-right { display: flex; align-items: center; gap: 14px; }
  .utility-right svg { display: block; }

  /* Sidebar */
  .sidebar {
    background: var(--ink);
    color: var(--sidebar-text);
    padding: 30px 26px 18px;
    display: flex; flex-direction: column;
  }
  .brand {
    display: flex; align-items: center; justify-content: center; gap: 9px;
    margin: 18px 0 26px;
    font-family: "Lato", sans-serif; font-weight: 700; font-size: 17px; color: #fff;
  }
  .brand-mark { width: 14px; height: 14px; background: var(--pink); flex: none; }
  .brand-blurb { font-size: 10.5px; line-height: 1.5; color: var(--sidebar-muted); text-align: center; margin-bottom: 26px; }
  .main-nav { list-style: none; text-align: center; margin-bottom: 34px; }
  .main-nav li {
    font-family: "Cormorant Garamond", serif; font-size: 14px; letter-spacing: 3px;
    padding: 6px 0; color: #fff;
  }
  .main-nav li:first-child { border-bottom: 1px solid var(--sidebar-muted); display: inline-block; padding-bottom: 4px; margin-bottom: 4px; }
  .newsletter-label { font-size: 9px; letter-spacing: 2px; text-align: center; margin-bottom: 8px; color: #fff; }
  .newsletter-form { display: flex; height: 20px; margin-bottom: 30px; }
  .newsletter-input { flex: 1; background: #fff; }
  .newsletter-button { width: 44px; background: var(--pink); color: #fff; font-size: 8px; display: flex; align-items: center; justify-content: center; letter-spacing: 1px; }
  .link-columns { display: grid; grid-template-columns: 1fr 1fr; gap: 14px; font-size: 11px; }
  .link-columns h3 { font-size: 11px; font-weight: 400; color: #fff; padding-bottom: 5px; margin-bottom: 6px; border-bottom: 1px solid var(--ink-soft); }
  .link-columns ul { list-style: none; }
  .link-columns li { padding: 3px 0; color: var(--sidebar-text); }
  .sidebar-footer { margin-top: auto; display: flex; justify-content: space-between; font-size: 11px; color: #fff; }

  /* Main area */
  .content { padding: 14px 16px 16px; display: flex; flex-direction: column; gap: 14px; }
  .hero {
    position: relative; height: 336px; flex: none;
    background: linear-gradient(100deg, var(--banner-light) 0%, #d6c8b3 45%, var(--banner-dark) 100%);
  }
  .hero-copy { position: absolute; right: 70px; top: 86px; text-align: center; }
  .hero-title {
    font-family: "Cormorant Garamond", serif; font-weight: 500; color: #fff;
    font-size: 44px; line-height: 1; letter-spacing: 3px; text-transform: uppercase;
  }
  .hero-button {
    display: inline-block; margin-top: 12px; background: var(--pink); color: #fff;
    font-size: 12px; letter-spacing: 2px; padding: 6px 16px;
  }
  .hero-arrow {
    position: absolute; top: 150px; width: 26px; height: 36px; background: var(--pink);
    display: flex; align-items: center; justify-content: center;
  }
  .hero-arrow.prev { left: 0; }
  .hero-arrow.next { right: 0; }

  .products { display: grid; grid-template-columns: repeat(4, 1fr); gap: 12px; flex: 1; min-height: 0; }
  .product-card { background: var(--card-bg); padding: 8px 8px 10px; display: flex; flex-direction: column; }
  .product-photo { height: 276px; background: linear-gradient(180deg, var(--photo-light), var(--photo-mid)); margin-bottom: 10px; }
  .product-head { display: flex; justify-content: space-between; font-size: 10px; color: var(--heading); margin-bottom: 5px; }
  .product-name { letter-spacing: 1px; text-transform: uppercase; }
  .product-desc { font-size: 9.5px; line-height: 1.45; margin-bottom: 8px; }
  .order-button { align-self: flex-start; background: var(--pink); color: #fff; font-size: 8.5px; letter-spacing: 1px; padding: 4px 12px; }
</style>
</head>
<body>
<div class="page">
  <header class="utility-bar">
    <ul class="utility-links">
      <li>My Account</li>
      <li>My Wishlist</li>
      <li>Checkout</li>
      <li>Log In</li>
    </ul>
    <div class="utility-right">
      <span>Shopping Cart : $0.00</span>
      <svg width="12" height="14" viewBox="0 0 12 14" aria-label="Cart"><rect x="1" y="4" width="10" height="9" fill="none" stroke="#fff" stroke-width="1.4"/><path d="M4 4V2.5a2 2 0 0 1 4 0V4" fill="none" stroke="#fff" stroke-width="1.4"/></svg>
      <svg width="13" height="13" viewBox="0 0 13 13" aria-hidden="true"><circle cx="6.5" cy="6.5" r="6" fill="#fff"/></svg>
      <svg width="13" height="13" viewBox="0 0 13 13" aria-hidden="true"><circle cx="6.5" cy="6.5" r="6" fill="#fff"/></svg>
      <svg width="13" height="13" viewBox="0 0 13 13" aria-label="Search"><circle cx="5.5" cy="5.5" r="4" fill="none" stroke="#fff" stroke-width="1.5"/><path d="M8.5 8.5l3.5 3.5" stroke="#fff" stroke-width="1.6"/></svg>
    </div>
  </header>

  <aside class="sidebar">
    <div class="brand"><span class="brand-mark"></span><span class="brand-name">Tessaly Lane Shop</span></div>
    <p class="brand-blurb">Fresh swimwear for sunny days, styled by our team and shipped quickly to your door from the coast.</p>
    <ul class="main-nav">
      <li>HOME</li>
      <li>PRODUCTS</li>
      <li>ABOUT</li>
      <li>SELLERS</li>
      <li>CONTACT</li>
    </ul>
    <p class="newsletter-label">NEWSLETTER</p>
    <div class="newsletter-form"><span class="newsletter-input"></span><span class="newsletter-button">SUBMIT</span></div>
    <div class="link-columns">
      <div>
        <h3>Our Offers</h3>
        <ul><li>New products</li><li>Top sellers</li><li>Specials</li><li>Manufacturers</li><li>Suppliers</li><li>Specials</li><li>Service</li></ul>
      </div>
      <div>
        <h3>Shipping Info</h3>
        <ul><li>Returns</li><li>Delivery</li><li>Service</li><li>Gift Cards</li><li>Mobile</li><li>Gift Cards</li><li>Manufacturers</li></ul>
      </div>
    </div>
    <div class="sidebar-footer"><span>Our Account</span><span>Our Support</span></div>
  </aside>

  <main class="content">
    <section class="hero" role="img" aria-label="Summer campaign photo of a model in a long gown seated on a chair outdoors">
      <span class="hero-arrow prev"><svg width="10" height="14" viewBox="0 0 10 14"><path d="M7 2L2 7l5 5" fill="none" stroke="#fff" stroke-width="2"/></svg></span>
      <div class="hero-copy">
        <h1 class="hero-title">Summer<br>Collection</h1>
        <span class="hero-button">SHOP NOW</span>
      </div>
      <span class="hero-arrow next"><svg width="10" height="14" viewBox="0 0 10 14"><path d="M3 2l5 5-5 5" fill="none" stroke="#fff" stroke-width="2"/></svg></span>
    </section>

    <section class="products">
      <article class="product-card">
        <div class="product-photo" role="img" aria-label="Product photo of a black lace bikini top worn by a model"></div>
        <div class="product-head"><span class="product-name">Black Nautic</span><span>$100.00</span></div>
        <p class="product-desc">Soft padded cups with adjustable straps, made for long days by the water.</p>
        <span class="order-button">ORDER</span>
      </article>
      <article class="product-card">
        <div class="product-photo" role="img" aria-label="Product photo of a pink bikini top worn by a model"></div>
        <div class="product-head"><span class="product-name">Pink Nautic</span><span>$100.00</span></div>
        <p class="product-desc">Bright ruched fabric with a gentle lift and a clasp that stays put.</p>
        <span class="order-button">ORDER</span>
      </article>
      <article class="product-card">
        <div class="product-photo" role="img" aria-label="Product photo of a black lace bikini top worn by a model"></div>
        <div class="product-head"><span class="product-name">Black Nautic</span><span>$100.00</span></div>
        <p class="product-desc">Classic lace trim over a smooth lining, cut for comfort and easy wear.</p>
        <span class="order-button">ORDER</span>
      </article>
      <article class="product-card">
        <div class="product-photo" role="img" aria-label="Product photo of a pink halter bikini top worn by a model"></div>
        <div class="product-head"><span class="product-name">Sunburst</span><span>$100.00</span></div>
        <p class="product-desc">Light halter style in warm pink, quick drying for sun and sea.</p>
        <span class="order-button">ORDER</span>
      </article>
    </section>
  </main>
</div>
</body>
</html>
```